Design Home Screen

We’re looking for talented UI/UX designers to create an eye-popping, modern, and fun Home Screen for the Plenk app — the future of real-time earned wage access and financial empowerment.
Your mission: make the Plenk experience come alive the moment users open the app.

Design Goals

The screen should instantly communicate energy, financial control, and trust.

The “Time on the Clock” and the “Plenk Balance” must be the stars of the screen — presented in a way that feels alive, interactive, and rewarding.

Think of how to visually celebrate a user’s progress at work and their earnings — something that makes checking the app feel fun and satisfying, not transactional.

Creative Direction

Style: Sleek, fintech-modern, with motion or visual elements that feel alive (micro-animations, glowing accents, gradient depth, or movement cues).

Tone: Confident, vibrant, and optimistic — this is a financial app that feels human and inspiring.

Color palette: Black, Gold, and Green, and any other color.

Typography: Clean, readable, and balanced between playful and professional.

Must-Have Elements

Time on the Clock – creatively displayed (e.g., countdown or progress animation as the user works).

Plenk Balance – bold, fun, and maybe even interactive (reflecting growth as the user earns).

A clean navigation structure for core tabs: Home, Access Pay, Boost, History, Profile.

Engaging micro-animations, icons, or progress indicators that make the user feel “in motion.”

Room for brand personality — the “Plenk” name and logo if desired.

```html
<!DOCTYPE html>
<html lang="en">
<head>
<meta charset="utf-8">
<title>Plenk Dashboard</title>
<link href="https://fonts.googleapis.com/css2?family=Inter:wght@400;500;600;700;800&display=swap" rel="stylesheet">
<style>
:root{
  --backdrop:#c8c8c8;
  --screen:#0f1729;
  --card:#141d31;
  --card-line:#27324a;
  --tile:#1c3650;
  --chip:#2a3446;
  --text:#ffffff;
  --muted:#aab3c3;
  --dim:#7f8898;
  --cyan:#7fe0f5;
  --green:#5fd08a;
  --gold:#e9b949;
  --amber:#f2c14e;
  --red:#ef5350;
  --blue:#2f6de3;
  --nav:#111a2c;
}
*{box-sizing:border-box;margin:0;padding:0}
html,body{width:1200px;height:2502px;overflow:hidden;background:var(--backdrop)}
body{font-family:"Inter",sans-serif;color:var(--text)}
.stage{position:absolute;left:0;top:0;width:614px;height:1280px;transform:scale(1.95440);transform-origin:0 0}
.screen{position:absolute;left:110px;top:95px;width:394px;height:1185px;background:var(--screen);border-radius:48px 48px 0 0;overflow:hidden}
.abs{position:absolute}
.center{transform:translateX(-50%);text-align:center;white-space:nowrap}
.title{left:197px;top:80px;font-size:20px;font-weight:700;letter-spacing:4px}
.avatar{left:14px;top:119px;width:42px;height:42px;border-radius:50%;border:2px solid var(--cyan);background:radial-gradient(circle at 50% 40%,#b78a6a,#4b3a30)}
.hello{left:67px;top:122px;font-size:11px;color:var(--muted)}
.user{left:67px;top:138px;font-size:15px;font-weight:700}
.top-icon{top:128px}
.media{left:74px;top:211px;width:56px;height:27px;background:#232b36}
.label{font-size:12px;color:var(--text)}
.balance{left:62px;top:284px;width:79px;height:42px;border-radius:5px;background:var(--chip);border-bottom:2px solid var(--gold);display:flex;align-items:center;justify-content:center;font-size:20px;font-weight:700;color:var(--cyan)}
.month{font-size:18px;font-weight:700;color:var(--cyan);letter-spacing:.5px}
.dates{font-size:15px}
.status span{color:var(--green);font-weight:600}
.hours{font-size:27px;font-weight:800;color:var(--cyan);letter-spacing:.5px}
.hours small{font-size:18px;font-weight:800}
.rate{font-size:15px}
.action{top:463px;width:56px;text-align:center}
.action .tile{width:56px;height:56px;border-radius:8px;background:var(--tile);display:flex;align-items:center;justify-content:center}
.action p{font-size:11px;line-height:14px;margin-top:8px;color:#dfe5ee;margin-left:-20px;margin-right:-20px}
.earn-amount{color:var(--gold)}
.transactions{left:14px;top:575px;width:364px;height:560px;background:var(--card);border:1px solid var(--card-line);border-radius:14px}
.tx-head{left:16px;top:18px;font-size:17px;font-weight:700}
.see-all{left:277px;top:20px;font-size:13px;color:var(--cyan)}
.tx-list{left:0;top:52px}
.tx{position:relative;width:364px;height:81px}
.tx + .tx{border-top:1px solid var(--card-line)}
.tx .mark{position:absolute;left:13px;top:20px;width:40px;height:40px;border-radius:50%}
.tx .name{position:absolute;left:64px;top:22px;font-size:14px;font-weight:700}
.tx .date{position:absolute;left:64px;top:41px;font-size:11px;color:var(--muted)}
.tx .amt{position:absolute;right:15px;top:15px;font-size:16px;font-weight:700;color:var(--cyan)}
.tx .state{position:absolute;right:15px;top:37px;font-size:11px;font-weight:600}
.tx .via{position:absolute;right:15px;top:52px;font-size:11px;color:var(--dim)}
.sent{color:var(--green)}.pending{color:var(--amber)}.failed{color:var(--red)}
.nav{left:0;top:1123px;width:394px;height:62px;background:var(--nav);border-top:1px solid var(--card-line)}
.nav-item{top:14px;width:60px;transform:translateX(-50%);text-align:center;font-size:10.5px;color:var(--muted);white-space:nowrap}
.nav-item svg{display:block;margin:0 auto 3px}
.nav-item.active{color:var(--cyan)}
.nav-item.boost{color:var(--gold)}
.switch{left:163px;top:1097px;width:66px;height:66px;border-radius:50%;background:var(--blue);border:3px solid #1c3f8a;box-shadow:0 0 18px rgba(47,109,227,.8);display:flex;flex-direction:column;align-items:center;justify-content:center;font-size:11px;font-weight:700;gap:2px}
</style>
</head>
<body>
<div class="stage">
  <main class="screen">
    <h1 class="abs center title">DASHBOARD</h1>

    <div class="abs avatar" role="img" aria-label="Profile photo of John Doe"></div>
    <p class="abs hello">Hello!</p>
    <p class="abs user">JOHN DOE</p>
    <svg class="abs top-icon" style="left:322px" width="20" height="16" viewBox="0 0 20 16" fill="none" stroke="#cfd6e2" stroke-width="1.6" stroke-linecap="round"><path d="M1 2h18M1 8h13M1 14h8"/></svg>
    <svg class="abs top-icon" style="left:358px;top:126px" width="20" height="20" viewBox="0 0 20 20" fill="none" stroke="#cfd6e2" stroke-width="1.5"><path d="M4 14V9a6 6 0 0 1 12 0v5l1.5 1.5h-15Z" stroke-linejoin="round"/><path d="M8 17.5a2 2 0 0 0 4 0"/><circle cx="15.5" cy="3.5" r="3" fill="var(--blue)" stroke="none"/></svg>

    <div class="abs media" role="img" aria-label="Balance illustration"></div>
    <p class="abs center label" style="left:101px;top:262px">Plenk Wage Balance:</p>
    <div class="abs balance">$10</div>
    <p class="abs center label" style="left:101px;top:349px">Current Pay Period:</p>
    <p class="abs center month" style="left:101px;top:373px">MARCH</p>
    <p class="abs center dates" style="left:101px;top:406px">1 - 15, 2025</p>

    <svg class="abs" style="left:248px;top:196px" width="84" height="84" viewBox="0 0 84 84">
      <circle cx="42" cy="42" r="42" fill="#f2f3f5"/>
      <circle cx="42" cy="42" r="35" fill="#27303b"/>
      <g stroke="#e8ecf0" stroke-width="1.6" stroke-linecap="round">
        <path d="M42 10v4M42 70v4M10 42h4M70 42h4M58 14.3l-2 3.5M28 66.2l-2 3.5M69.7 26l-3.5 2M17.8 56l-3.5 2M69.7 58l-3.5-2M17.8 28l-3.5-2M58 69.7l-2-3.5M28 17.8l-2-3.5"/>
      </g>
      <path d="M42 42V14" stroke="#fff" stroke-width="3" stroke-linecap="round"/>
      <path d="M42 42v9" stroke="#fff" stroke-width="3" stroke-linecap="round"/>
      <circle cx="42" cy="42" r="2.5" fill="var(--gold)"/>
    </svg>
    <p class="abs center label status" style="left:290px;top:289px">Status: <span>On the Clock</span></p>
    <p class="abs center label" style="left:290px;top:328px">Work Hours:</p>
    <p class="abs center hours" style="left:290px;top:349px">19:00 <small>HRS.</small></p>
    <p class="abs center rate" style="left:290px;top:390px">@ $20.00/hr</p>

    <div class="abs action" style="left:32px">
      <div class="tile"><svg width="24" height="24" viewBox="0 0 24 24" fill="none" stroke="var(--cyan)" stroke-width="1.7" stroke-linecap="round" stroke-linejoin="round"><path d="M12 3v12M7 10l5 5 5-5M4 16v4h16v-4"/></svg></div>
      <p>Request<br>Money</p>
    </div>
    <div class="abs action" style="left:123px">
      <div class="tile"><svg width="26" height="26" viewBox="0 0 26 26" fill="none" stroke="var(--cyan)" stroke-width="1.6" stroke-linejoin="round"><path d="M3 9 13 3l10 6H3ZM5 11v9M9 11v9M13 11v9M17 11v9M21 11v9M3 22h20"/></svg></div>
      <p>Loan Access</p>
    </div>
    <div class="abs action" style="left:214px">
      <div class="tile"><svg width="24" height="24" viewBox="0 0 24 24" fill="none" stroke="var(--cyan)" stroke-width="1.8" stroke-linecap="round"><path d="M12 3v18M3 12h18"/></svg></div>
      <p>Update<br>Employment</p>
    </div>
    <div class="abs action" style="left:305px">
      <div class="tile"><svg width="24" height="24" viewBox="0 0 24 24" fill="none" stroke="var(--cyan)" stroke-width="1.6" stroke-linecap="round"><rect x="6" y="2" width="12" height="20" rx="2.5"/><path d="M10 8h4M10 12h4M10 16h4"/></svg></div>
      <p>Earn<br><span class="earn-amount">$7,500</span></p>
    </div>

    <section class="abs transactions">
      <h2 class="abs tx-head">Transactions:</h2>
      <span class="abs see-all">See All</span>
      <svg class="abs" style="left:333px;top:21px" width="16" height="14" viewBox="0 0 16 14" fill="none" stroke="#cfd6e2" stroke-width="1.5" stroke-linecap="round"><path d="M1 2h14M1 7h10M1 12h6"/></svg>

      <div class="abs tx-list">
        <div class="tx">
          <div class="mark" role="img" aria-label="Profile photo of John Doe" style="background:radial-gradient(circle at 50% 40%,#b78a6a,#4b3a30)"></div>
          <p class="name">John Doe Inc.</p><p class="date">July 12, 2025</p>
          <p class="amt">$350.50</p><p class="state sent">Sent</p><p class="via">Via PayLoop</p>
        </div>
        <div class="tx">
          <div class="mark" style="background:#7a5bb0"></div>
          <p class="name">Lorvan Inc.</p><p class="date">July 10, 2025</p>
          <p class="amt">$280.75</p><p class="state sent">Sent</p><p class="via">Via PayLoop</p>
        </div>
        <div class="tx">
          <div class="mark" style="background:#3aa335"></div>
          <p class="name">Gigwell</p><p class="date">July 03, 2025</p>
          <p class="amt">$1300.00</p><p class="state pending">Pending</p><p class="via">Via Sendly</p>
        </div>
        <div class="tx">
          <div class="mark" style="background:#1b2f63"></div>
          <p class="name">Bloomfield Goods</p><p class="date">June 23, 2025</p>
          <p class="amt">$75.00</p><p class="state sent">Sent</p><p class="via">Via Strata</p>
        </div>
        <div class="tx">
          <div class="mark" style="background:#f0525e"></div>
          <p class="name">StayNest</p><p class="date">June 17, 2025</p>
          <p class="amt">$450.00</p><p class="state sent">Sent</p><p class="via">Via Zipto</p>
        </div>
        <div class="tx">
          <div class="mark" style="background:#6f8a7a"></div>
          <p class="name">Alder Clinic</p><p class="date">June 12, 2025</p>
          <p class="amt">$157.35</p><p class="state failed">Failed</p><p class="via">Via PayLoop</p>
        </div>
      </div>
    </section>

    <nav class="abs nav">
      <div class="abs nav-item active" style="left:40px">
        <svg width="20" height="20" viewBox="0 0 20 20" fill="none" stroke="currentColor" stroke-width="1.5" stroke-linejoin="round"><path d="M3 9 10 3l7 6v8h-5v-5H8v5H3Z"/></svg>Home</div>
      <div class="abs nav-item" style="left:112px">
        <svg width="20" height="20" viewBox="0 0 20 20" fill="none" stroke="currentColor" stroke-width="1.5" stroke-linejoin="round"><rect x="2.5" y="5" width="15" height="11" rx="2"/><path d="M2.5 8.5h15M13 12.5h2"/></svg>Access Pay</div>
      <div class="abs nav-item boost" style="left:260px">
        <svg width="20" height="20" viewBox="0 0 20 20" fill="none" stroke="currentColor" stroke-width="1.5" stroke-linejoin="round"><path d="M11.5 2 4.5 11h5l-1 7 7-9h-5Z"/></svg>Boost</div>
      <div class="abs nav-item" style="left:315px">
        <svg width="20" height="20" viewBox="0 0 20 20" fill="none" stroke="currentColor" stroke-width="1.5" stroke-linejoin="round"><path d="M5 2h7l4 4v12H5Z"/><path d="M8 10h5M8 13h5"/></svg>History</div>
      <div class="abs nav-item" style="left:366px">
        <svg width="20" height="20" viewBox="0 0 20 20" fill="none" stroke="currentColor" stroke-width="1.5"><circle cx="10" cy="6.5" r="3.5"/><path d="M3 18c0-4 3-6 7-6s7 2 7 6Z" stroke-linejoin="round"/></svg>Profile</div>
    </nav>
    <div class="abs switch">
      <svg width="22" height="20" viewBox="0 0 22 20" fill="none" stroke="#fff" stroke-width="1.8" stroke-linecap="round" stroke-linejoin="round"><path d="M3 6h15M14 2l4 4-4 4M19 14H4M8 10l-4 4 4 4"/></svg>
      Switch
    </div>
  </main>
</div>
</body>
</html>
```